Principal Licensure: MVL Cohort

I am writing to you from the office of Extended & Career Learning within the College of Teaching & Civic Growth at the Halvern Ridge University. We offer professional education and learning opportunities to educators in Colorado. We are looking for a brochure design for our new program that prepares aspiring leaders to apply for principal licensure to become a school principal. The program is called the "MVL Cohort." We are partnering with Tamsworth Unified Schools (http://www.guidetamsworth.example/) to offer the program. Both of our organizations value innovation, urban schools and school reform. The final design should communicate leadership, equity and diversity and thinking outside of the box. Unfortunately, we do not have any images on hand so we welcome any image proposals. Images should reflect ethnic, age, and gender diversity. Images should include professionals that are interacting with students (adult or children) or with one another in an educational and collaborative setting.
Is there any way to design the brochure so it may be sent via email as well?

Hi everyone! I posted a couple more logos in case they might be a better fit for the designs. Thanks!
Greta

Target Market(s)

Educators and business professionals 30-45 years old who are passionate about urban schools and education reform.

Industry/Entity Type

Education

Requirements
Must have
• The brochure must include all text that is attached. I have attached a few of our other pieces to give you an idea of what we already work with. We would like this one to look associated but also have a distinct look, tailored to professionals. We really like the arrow and the color bar that is a part of our header (see attached brochure) It should also include the HRU and TUS logos (also attached). We are not committed to particular colors but I have attached a color palette.
Should not have
• It should not include overplayed education images such as apples, chalkboards, students sitting in desks with their hands raised. We want to convey a collaborative approach that attracts leaders and business professionals. We are looking for color and something different than the standard education imagery.

```html
<!DOCTYPE html>
<html lang="en">
<head>
<meta charset="utf-8">
<title>MVL Cohort – Back Cover</title>
<link rel="stylesheet" href="https://fonts.googleapis.com/css2?family=Maven+Pro:wght@400;500&display=swap">
<style>
  :root {
    --stage: #ecebe8;
    --paper: #f3f3f4;
    --brand-red: #b5121b;
    --ink-white: #ffffff;
    --ink-grey: #5f6368;
    --logo-blue: #2f6fae;
  }
  * { margin: 0; padding: 0; box-sizing: border-box; }
  html, body {
    width: 1200px; height: 803px; overflow: hidden;
    background: var(--stage);
    font-family: "Maven Pro", "Helvetica Neue", Arial, sans-serif;
  }
  .back-cover {
    position: absolute; left: 340px; top: 42px;
    width: 520px; height: 720px;
    background: var(--paper);
    box-shadow: 0 6px 18px rgba(0,0,0,0.18);
    overflow: hidden;
  }
  .cover-shapes { position: absolute; inset: 0; }
  .cover-shapes .red { fill: var(--brand-red); }

  .services {
    position: absolute; left: 34px; top: 34px; width: 450px;
    color: var(--ink-white);
  }
  .services-title { font-size: 22px; font-weight: 500; line-height: 1.1; margin-bottom: 8px; }
  .services-body { font-size: 7.5px; line-height: 1.45; }

  .contact {
    position: absolute; left: 236px; top: 232px; width: 260px;
    color: var(--ink-white);
  }
  .contact-title { font-size: 17px; font-weight: 400; margin-bottom: 8px; }
  .contact-lines { font-size: 9.5px; line-height: 1.3; font-style: normal; }

  .partner-mark {
    position: absolute; left: 30px; top: 372px;
    display: flex; align-items: center; gap: 6px;
  }
  .partner-mark .mark-square {
    width: 22px; height: 22px; background: var(--logo-blue);
  }
  .partner-mark .mark-name {
    font-size: 10px; font-weight: 500; color: var(--logo-blue);
    line-height: 1.1; width: 80px;
  }

  .legal {
    position: absolute; left: 34px; bottom: 40px; width: 452px;
    font-size: 4.6px; line-height: 1.5; color: var(--ink-grey);
  }
</style>
</head>
<body>
  <article class="back-cover">
    <svg class="cover-shapes" width="520" height="720" viewBox="0 0 520 720" aria-hidden="true">
      <path class="red" d="M0 0 H520 V140 Q300 180 0 245 Z"/>
      <path class="red" d="M190 228 Q340 188 520 160 V380 H190 Z"/>
    </svg>

    <section class="services">
      <h2 class="services-title">Get to know more about our services</h2>
      <p class="services-body">The MVL Cohort prepares aspiring school leaders for principal licensure through a shared program of Halvern Ridge University and Tamsworth Unified Schools. Participants learn together in small groups, work alongside mentor principals, and lead real projects in urban schools. Sessions meet evenings and weekends so working educators and professionals can join while they continue in their current roles across the district.</p>
    </section>

    <section class="contact">
      <h2 class="contact-title">Stay In Touch</h2>
      <address class="contact-lines">
        1728 Larkspur Avenue, Tamsworth,<br>
        CO 80000<br>
        T: 1-555-210-4830<br>
        E: hello@mvlcohort.example<br>
        W: www.mvlcohort.example
      </address>
    </section>

    <div class="partner-mark">
      <span class="mark-square"></span>
      <span class="mark-name">Tamsworth Unified Schools</span>
    </div>

    <p class="legal">© 2024 Halvern Ridge University. All rights reserved. The MVL Cohort is offered by Extended &amp; Career Learning within the College of Teaching &amp; Civic Growth in partnership with Tamsworth Unified Schools. Program dates, fees and requirements may change without notice. Admission is open to licensed educators and qualified professionals who meet state requirements for principal licensure. For current details, schedules and application steps, please visit our website or contact the program office directly by phone or email during regular business hours.</p>
  </article>
</body>
</html>
```